AUTOMOTIVE/ CAR REPAIRS / CRASH REPAIRS / PAINT SPRAYING AND PANEL BEATING

AUTOMOTIVE REPAIR. CAR / MOTORCYCLES GOT LOGO DESIGN / DID THINK ABOUT CHATTERLY DONT NOALREADY HAVE WEB ADRESS www.veltrashine.co.uk and mail sales@veltrashine,co.uk NEED SOMETHINK I CAN MANAGE TO UPLOAD PICTURES IN TO A GALLERY OR SOMETHINGLIKE THAT I ALSO SELL CAR AND MOTORCYCLES MAYBE A SELLS PAGE WITH A COINSEND LINK

Target Market(s)

TRADE / GENERAL PUBLIC

Industry/Entity Type

Automotive

Coding

Coded - Design and coding required

Number of Pages Required

4 page

Font styles to use
Serif
Sans Serif

Colors

Designer to choose colors to be used in the design.

Requirements
Must have
• GALLERY/ SHOP TO SALE CARS AND MOTORCYCLE / LOGOS OF MATERIALS I USE ZELWORTH / KIBO / TASCANI / Q BAND / GLEAMFORD
• CONTACT US
Nice to have
• COINSEND / EASY TO MANAGE / VIDEO CLIP OF ZELWORTH FLOWDESK Z4
• TRUEBLEND PAINT VOLANTA FERROLUX AND BELNOVA

```html
<!DOCTYPE html>
<html lang="en">
<head>
<meta charset="utf-8">
<title>Veltrashine Bodyshop</title>
<link href="https://fonts.googleapis.com/css2?family=Roboto:wght@300;400;500;700&display=swap" rel="stylesheet">
<style>
:root{
  --red:#e3161b;
  --navy:#1c1f2e;
  --ink:#2b2b2b;
  --muted:#555;
  --line:#cfcfcf;
  --white:#fff;
  --gold:#c9a227;
}
*{box-sizing:border-box;margin:0;padding:0}
html,body{width:1200px;height:5333px;overflow:hidden}
body{position:relative;background:var(--white);font-family:'Roboto',sans-serif;color:var(--ink)}
.abs{position:absolute}
.btn{position:absolute;background:var(--red);color:#fff;font-size:12px;display:flex;align-items:center;justify-content:center}
.sec-title{position:absolute;left:0;width:1200px;text-align:center;font-size:31px;font-weight:400;color:var(--ink)}
/* top bar */
.topbar{left:0;top:0;width:1200px;height:31px;background:#fff;font-size:12px;color:#444}
.topbar .lang{left:79px;top:8px}
.topbar .phone{left:545px;top:8px;display:flex;gap:8px;align-items:center}
.topbar .social{right:0;top:0;width:290px;height:31px;background:var(--red);clip-path:polygon(12% 0,100% 0,100% 100%,0 100%);display:flex;justify-content:flex-end;gap:22px;align-items:center;padding-right:22px;color:#fff;font-size:12px;font-weight:700}
/* nav */
.nav{left:0;top:31px;width:1200px;height:103px;background:var(--navy)}
.brand{color:#fff;font-size:30px;font-weight:500;letter-spacing:3px;display:flex;align-items:center;gap:10px}
.brand i{display:block;width:14px;height:14px;border-radius:50%;background:var(--red)}
.nav .brand{left:85px;top:32px}
.nav ul{position:absolute;left:502px;top:38px;display:flex;gap:36px;list-style:none;color:#fff;font-size:14px}
.nav ul li.active{border-bottom:2px solid #fff;padding-bottom:4px}
/* hero */
.hero{left:0;top:134px;width:1200px;height:566px;background:linear-gradient(100deg,#1d1e22 0%,#45474d 45%,#8a8d93 70%,#b9bcc2 100%)}
.hero h1{position:absolute;left:227px;top:166px;color:#fff;font-size:32px;font-weight:400}
.hero p{position:absolute;left:227px;top:210px;color:#fff;font-size:14px;line-height:18px}
.badge{left:95px;top:172px;width:114px;height:114px;border-radius:50%;background:radial-gradient(circle,#e2c15a,#8a6a14)}
.hero .arrow{position:absolute;top:190px;width:32px;height:32px;border:2px solid rgba(255,255,255,.8);border-radius:50%}
.dots{display:flex;gap:8px}
.dots span{width:7px;height:7px;border-radius:50%;background:#ccc}
.dots span.on{background:var(--red)}
/* about */
.about h3{left:79px;top:852px;width:500px;font-size:20px;font-weight:400;line-height:24px;color:#222}
.about .txt{left:79px;top:922px;width:500px;font-size:12px;line-height:16px;color:#444}
.about .img{left:592px;top:797px;width:546px;height:423px;background:linear-gradient(160deg,#f2f2f2,#c2c2c4 60%,#8b1c1e);border-radius:4px}
/* services */
.card{position:absolute;top:1382px;width:240px;height:267px;border:2px solid var(--line);background:#fff;text-align:center}
.card .ico{width:80px;height:80px;margin:28px auto 10px;background:#e6e6e6;border-radius:8px}
.card h4{font-size:19px;font-weight:500;color:#222}
.card p{font-size:12px;line-height:16px;color:#555;margin:10px 24px 0}
.card svg{margin-top:16px}
.card.hot{background:var(--red);border-color:var(--red)}
.card.hot h4,.card.hot p{color:#fff}
.card.hot .ico{background:rgba(255,255,255,.35)}
/* tutorial */
.tutorial{left:0;top:1790px;width:1200px;height:501px;background:var(--navy);color:#fff}
.tutorial h2{position:absolute;left:79px;top:84px;font-size:30px;font-weight:500}
.tutorial .txt{position:absolute;left:79px;top:156px;width:482px;font-size:12px;line-height:16px}
.video{left:590px;top:76px;width:540px;height:346px;background:#fff;padding:12px}
.video .scr{width:100%;height:100%;background:linear-gradient(120deg,#141a3a,#2b3b8f 40%,#6d7fbf 70%,#c9ccd6);position:relative}
.video .cap{position:absolute;left:150px;bottom:18px;font-size:15px;color:#fff;text-align:center;line-height:18px}
.video .play{position:absolute;left:245px;top:140px;width:60px;height:40px;background:var(--red);border-radius:10px}
.video .play:after{content:"";position:absolute;left:24px;top:11px;border-left:16px solid #fff;border-top:9px solid transparent;border-bottom:9px solid transparent}
/* products */
.tabs{left:0;top:2398px;width:1200px;text-align:center;font-size:13px;color:#333;word-spacing:4px}
.tabs b{color:var(--red);font-weight:400}
.viewall{left:990px;top:2398px;font-size:13px;text-decoration:underline;color:#333}
.prod{position:absolute;top:2431px;width:240px}
.prod .ph{height:286px;border:1px solid #ddd;display:flex;align-items:center;justify-content:center}
.prod .ph div{width:210px;height:130px;border-radius:30px 30px 10px 10px}
.prod .name{text-align:center;font-size:12px;font-weight:500;margin-top:18px}
.prod .price{text-align:center;font-size:12px;color:var(--red);margin-top:6px}
.prod .stars{text-align:center;font-size:11px;color:var(--gold);margin-top:4px;letter-spacing:1px}
.side-arrow{position:absolute;font-size:20px;color:#999}
/* custom */
.custom{left:0;top:2859px;width:1200px;height:501px;background:linear-gradient(90deg,#2d2a28,#5a5550 50%,#8e8a86 80%,#3e3a37)}
.custom .box{position:absolute;left:79px;top:85px;width:395px;height:329px;background:var(--red);color:#fff;padding:38px 36px}
.custom h2{font-size:31px;font-weight:400;letter-spacing:1px}
.custom p{font-size:12px;line-height:15px;margin-top:22px}
.custom ul{list-style:none;font-size:12px;line-height:16px;margin-top:12px}
.custom ul li:before{content:"○ ";font-size:10px}
.custom .btn{position:static;width:168px;height:40px;background:var(--navy);margin-top:24px}
/* gallery */
.gal{position:absolute}
/* testimonials */
.testi{position:absolute;top:4165px;width:333px;height:329px;border:2px solid #ddd;text-align:center}
.testi .q{position:absolute;left:18px;top:-2px;width:44px;height:36px;background:var(--red);color:#fff;font-size:34px;font-weight:700;line-height:44px}
.testi .av{width:112px;height:112px;border-radius:50%;background:#b8bcc4;margin:22px auto 10px}
.testi h5{font-size:16px;font-weight:400;color:#333}
.testi .role{font-size:14px;color:var(--red)}
.testi p{font-size:13px;line-height:17px;color:#555;margin:12px 40px 0}
.testi .stars{color:var(--gold);font-size:11px;margin-top:4px}
.testi .more{font-size:14px;color:#555;margin-top:8px}
/* partners */
.partner{position:absolute;top:4618px;width:190px;height:122px;border:1px solid #e0e0e0;display:flex;align-items:center;justify-content:center;font-size:22px;font-weight:700;color:#333}
/* footer */
.footer{left:0;top:4817px;width:1200px;height:465px;background:var(--navy);color:#fff}
.footer h6{position:absolute;top:186px;font-size:17px;font-weight:400}
.footer .info{position:absolute;left:79px;top:240px;font-size:13px;line-height:17px}
.footer .row{display:flex;gap:12px;margin-bottom:22px}
.field{position:absolute;border:1px solid #8a8da0;font-size:12px;padding:6px 8px;color:#ddd}
.bottom{left:0;top:5282px;width:1200px;height:51px;background:#fff;font-size:11px;color:#333}
.pay{position:absolute;top:14px;height:26px;width:52px;border-radius:3px;color:#fff;font-size:9px;font-weight:700;display:flex;align-items:center;justify-content:center}
</style>
</head>
<body>

<header class="abs topbar">
  <div class="abs lang">Eng ▾ &nbsp; | &nbsp; USD ▾</div>
  <div class="abs phone"><svg width="12" height="12" viewBox="0 0 24 24"><path fill="#333" d="M6.6 10.8a15 15 0 006.6 6.6l2.2-2.2c.3-.3.7-.4 1-.2 1.1.4 2.3.6 3.6.6.6 0 1 .4 1 1V20c0 .6-.4 1-1 1A17 17 0 013 4c0-.6.4-1 1-1h3.5c.6 0 1 .4 1 1 0 1.3.2 2.5.6 3.6.1.3 0 .7-.2 1z"/></svg>07700 900512</div>
  <div class="abs social"><span>C</span><span>H</span><span>S</span><span>L</span></div>
</header>

<nav class="abs nav">
  <div class="abs brand">VELTRASHINE<i></i></div>
  <ul>
    <li class="active">Home</li><li>About us</li><li>Service ▾</li><li>Custom</li><li>Gallery</li><li>Contact us</li>
  </ul>
  <svg class="abs" style="left:1055px;top:38px" width="18" height="18" viewBox="0 0 24 24"><circle cx="10" cy="10" r="7" fill="none" stroke="#fff" stroke-width="2"/><path d="M15 15l6 6" stroke="#fff" stroke-width="2"/></svg>
  <svg class="abs" style="left:1096px;top:36px" width="22" height="22" viewBox="0 0 24 24"><path d="M2 4h3l3 11h11l2-8H7" fill="none" stroke="#fff" stroke-width="2"/><circle cx="9" cy="19" r="1.6" fill="#fff"/><circle cx="18" cy="19" r="1.6" fill="#fff"/><circle cx="20" cy="4" r="3" fill="#e3161b"/></svg>
</nav>

<section class="abs hero" role="img" aria-label="Technician in protective suit spray painting a car">
  <div class="abs badge" role="img" aria-label="Quality guarantee badge"></div>
  <h1>AUTOMOTIVE</h1>
  <p>CAR / CRASH REPAIRS / PAINT SPRAYING<br>&amp; PANEL BEATING</p>
  <div class="btn" style="left:227px;top:264px;width:168px;height:40px">Get a Quote</div>
  <div class="arrow" style="left:38px"></div>
  <div class="arrow" style="left:1138px"></div>
  <div class="abs dots" style="left:576px;top:516px"><span class="on"></span><span></span><span></span><span></span></div>
  <svg class="abs" style="left:0;top:466px" width="1200" height="100" viewBox="0 0 1200 100" preserveAspectRatio="none"><path d="M0 40 Q600 110 1200 0 L1200 100 L0 100Z" fill="#fff"/><path d="M0 40 Q600 110 1200 0 L1200 14 Q600 120 0 46Z" fill="#e3161b"/></svg>
</section>

<section class="about">
  <h2 class="sec-title" style="top:758px">About us</h2>
  <h3 class="abs">Fully qualified trained technicians family run business established over 30 years</h3>
  <div class="abs txt">
    <p>Your company did a great job on my Halden Coupe. I was very pleased with the service you provided and the extra attention to detail. I would recommend Veltrashine to anyone needing any sort of car body repairs "</p><br>
    <p>Veltrashine, based in Ashwell, Derbyshire established in August, 1985 has grown to become Derbyshire's premiere manufacturer approved accident repair centre.<br>Equipped with the latest technology and factory trained technicians, we process accident repairs for all leading insurance and vehicle management companies, specialising in accident repairs for most prestige vehicles manufacturers. We are proud to maintain a close working partnership with several local dealership networks..</p>
  </div>
  <div class="btn" style="left:79px;top:1146px;width:168px;height:42px">Read More</div>
  <div class="abs img" role="img" aria-label="Mechanic working on a motorcycle on a lift"></div>
</section>

<section class="services">
  <h2 class="sec-title" style="top:1292px">Our Service</h2>
  <div class="card" style="left:79px"><div class="ico" role="img" aria-label="Spray gun icon"></div><h4>Full or Part Resprays</h4><p>Lorem Ipsum is simply dummy text of the printing and typeset in the industry.</p><svg width="28" height="28" viewBox="0 0 28 28"><circle cx="14" cy="14" r="12" fill="none" stroke="#333" stroke-width="1.5"/><path d="M9 14h10M15 10l4 4-4 4" fill="none" stroke="#333" stroke-width="1.5"/></svg></div>
  <div class="card hot" style="left:345px"><div class="ico" role="img" aria-label="Dented car icon"></div><h4>Dent &amp; Scratch</h4><p>Lorem Ipsum is simply dummy text of the printing and typeset in the industry.</p><svg width="28" height="28" viewBox="0 0 28 28"><circle cx="14" cy="14" r="12" fill="none" stroke="#fff" stroke-width="1.5"/><path d="M9 14h10M15 10l4 4-4 4" fill="none" stroke="#fff" stroke-width="1.5"/></svg></div>
  <div class="card" style="left:613px"><div class="ico" role="img" aria-label="Bumper icon"></div><h4>Bumper Repair</h4><p>Lorem Ipsum is simply dummy text of the printing and typeset in the industry.</p><svg width="28" height="28" viewBox="0 0 28 28"><circle cx="14" cy="14" r="12" fill="none" stroke="#333" stroke-width="1.5"/><path d="M9 14h10M15 10l4 4-4 4" fill="none" stroke="#333" stroke-width="1.5"/></svg></div>
  <div class="card" style="left:879px"><div class="ico" role="img" aria-label="Car collision icon"></div><h4>Accident repair</h4><p>Lorem Ipsum is simply dummy text of the printing and typeset in the industry.</p><svg width="28" height="28" viewBox="0 0 28 28"><circle cx="14" cy="14" r="12" fill="none" stroke="#333" stroke-width="1.5"/><path d="M9 14h10M15 10l4 4-4 4" fill="none" stroke="#333" stroke-width="1.5"/></svg></div>
  <div class="btn" style="left:515px;top:1684px;width:168px;height:44px">View More</div>
</section>

<section class="abs tutorial">
  <h2>Tutorial Flowdesk Z4</h2>
  <div class="txt">
    <p>Lorem Ipsum is simply dummy text of the printing Lorem Ipsum has been the industry's standard dummy text ever since the 1500s,</p><br>
    <p>when an unknown printer took a galley of type and scrambled it to make a type specimen book. It has survived not only five centuries, but also the leap into electronic typesetting, remaining essentially unchanged.</p><br>
    <p>It was 1960s with the release of Tessaprint sheets containing Lorem Ipsum passages, and more recently with desktop publishing software like Pagewright including versions of Lorem Ipsum.</p>
  </div>
  <div class="btn" style="left:79px;top:356px;width:168px;height:42px">Read More</div>
  <div class="abs video">
    <div class="scr" role="img" aria-label="Video still of a presenter beside a paint mixing wheel">
      <div class="play"></div>
      <div class="cap">Hai trovato un chip a colori usando<br>il software Flowdesk Z4.</div>
    </div>
  </div>
</section>

<section class="products">
  <h2 class="sec-title" style="top:2346px">Fetured Products</h2>
  <div class="abs tabs"><b>All</b> &nbsp; | &nbsp; Car &nbsp; | &nbsp; Bike &nbsp; | &nbsp; Accessories</div>
  <div class="abs viewall">View More Product</div>
  <div class="side-arrow" style="left:30px;top:2572px">←</div>
  <div class="side-arrow" style="left:1150px;top:2590px">→</div>
  <div class="prod" style="left:79px"><div class="ph"><div role="img" aria-label="Brown SUV" style="background:linear-gradient(#7a5a46,#3a2a22)"></div></div><div class="name">Brown Corvane GLX</div><div class="price">$ 00.00</div><div class="stars">★★★★★</div></div>
  <div class="prod" style="left:341px"><div class="ph"><div role="img" aria-label="Blue hatchback" style="background:linear-gradient(#3a4a8c,#161f4a)"></div></div><div class="name">Novaro</div><div class="price">$ 00.00</div><div class="stars">★★★★★</div></div>
  <div class="prod" style="left:606px"><div class="ph"><div role="img" aria-label="Black motorcycle" style="background:linear-gradient(#6a6a6a,#1d1d1d);width:110px;height:200px"></div></div><div class="name">Fishing Clothing Men</div><div class="price">$ 00.00</div><div class="stars">★★★★★</div></div>
  <div class="prod" style="left:871px"><div class="ph"><div role="img" aria-label="Dark grey saloon" style="background:linear-gradient(#6c6f74,#2c2e31)"></div></div><div class="name">2013 Stellan S4</div><div class="price">$ 00.00</div><div class="stars">★★★★★</div></div>
</section>

<section class="abs custom" role="img" aria-label="Custom motorcycle and silver car in a workshop">
  <div class="box">
    <h2>CUSTOMISATION</h2>
    <p>Our experienced team can efficiently carry out any customising work you require in order to meet the specific design you have in mind.</p>
    <ul><li>Full or part resprays</li><li>Dents &amp; scratch removal</li><li>Bumper repair</li><li>Accident repair</li><li>Alloy wheel's refurbished, repaired &amp; painted</li></ul>
    <div class="btn">Read More</div>
  </div>
</section>

<section class="gallery">
  <h2 class="sec-title" style="top:3406px">Gallery</h2>
  <div class="gal" role="img" aria-label="Hand polishing a red car" style="left:79px;top:3466px;width:333px;height:219px;background:linear-gradient(135deg,#f0d9cc,#d42a25 60%,#7d1010)"></div>
  <div class="gal" role="img" aria-label="Painter spraying in a paint booth, video" style="left:432px;top:3466px;width:334px;height:283px;background:linear-gradient(#5a5a5c,#2a2a2c)">
    <svg style="position:absolute;left:135px;top:110px" width="64" height="64" viewBox="0 0 64 64"><circle cx="32" cy="32" r="29" fill="none" stroke="#fff" stroke-width="2"/><path d="M26 20l18 12-18 12z" fill="none" stroke="#fff" stroke-width="2"/></svg>
  </div>
  <div class="gal" role="img" aria-label="Car wheel at sunset" style="left:786px;top:3466px;width:333px;height:219px;background:linear-gradient(135deg,#f4c88a,#7b8aa0 50%,#2e3440)"></div>
  <div class="gal" role="img" aria-label="Oil pouring into an engine" style="left:79px;top:3708px;width:333px;height:279px;background:linear-gradient(135deg,#c8cdd3,#5f6770 50%,#c8921c)"></div>
  <div class="gal" role="img" aria-label="Sparks from grinding metal" style="left:432px;top:3770px;width:334px;height:217px;background:linear-gradient(135deg,#3a3634,#1b1a19 60%,#d98a2a)"></div>
  <div class="gal" role="img" aria-label="Mechanic working under a car bonnet" style="left:786px;top:3708px;width:333px;height:279px;background:linear-gradient(135deg,#b9bec6,#3b5a9a 55%,#1c2642)"></div>
  <div class="btn" style="left:518px;top:4018px;width:168px;height:41px">View More</div>
</section>

<section class="testimonials">
  <h2 class="sec-title" style="top:4108px">Testimonials</h2>
  <div class="testi" style="left:79px"><div class="q">“</div><div class="av" role="img" aria-label="Customer portrait"></div><h5>Daniel</h5><div class="role">Director</div><p>Lorem Ipsum is simply dummy of the printing and typesetting lorem Ipsum industry.</p><div class="stars">★★★★★</div><div class="more">Read More.. ⊕</div></div>
  <div class="testi" style="left:433px"><div class="q">“</div><div class="av" role="img" aria-label="Customer portrait"></div><h5>Marcus</h5><div class="role">Director</div><p>Lorem Ipsum is simply dummy of the printing and typesetting lorem Ipsum industry.</p><div class="more" style="margin-top:24px">Read More.. ⊕</div></div>
  <div class="testi" style="left:786px"><div class="q">“</div><div class="av" role="img" aria-label="Customer portrait"></div><h5>Helen Carter</h5><div class="role">Director</div><p>Lorem Ipsum is simply dummy of the printing and typesetting lorem Ipsum industry.</p><div class="more" style="margin-top:24px">Read More.. ⊕</div></div>
  <div class="abs dots" style="left:580px;top:4524px"><span class="on"></span><span></span><span></span></div>
</section>

<section class="partners">
  <h2 class="sec-title" style="top:4561px">Partner</h2>
  <div class="side-arrow" style="left:32px;top:4664px">‹</div>
  <div class="side-arrow" style="left:1156px;top:4664px">›</div>
  <div class="partner" style="left:79px">ZELWORTH</div>
  <div class="partner" style="left:292px">TASCANI</div>
  <div class="partner" style="left:505px">Q BAND</div>
  <div class="partner" style="left:718px">GLEAMFORD</div>
  <div class="partner" style="left:929px">KIBO</div>
</section>

<footer class="abs footer">
  <svg class="abs" style="left:0;top:-1px" width="1200" height="60" viewBox="0 0 1200 60" preserveAspectRatio="none"><path d="M0 0 H1200 V30 Q600 -30 0 30Z" fill="#fff"/><path d="M0 30 Q600 -30 1200 30 L1200 36 Q600 -20 0 36Z" fill="#e3161b"/></svg>
  <div class="abs brand" style="left:463px;top:70px">VELTRASHINE<i></i></div>
  <h6 style="left:79px">Contact us</h6>
  <h6 style="left:414px">Quick Contact</h6>
  <h6 style="left:818px">Our Location</h6>
  <div class="info">
    <div class="row"><span>⌖</span><span>Harrow Trade Park, Kiln Road,<br>Ashwell, Derbyshire, DE71 9QX</span></div>
    <div class="row" style="margin-bottom:4px"><span>☏</span><span>07700 900512</span></div>
    <div class="row"><span>✉</span><span>sales@veltrashine,co.uk</span></div>
    <div class="row" style="gap:6px;font-size:11px"><span>ⓒ</span><span>ⓗ</span><span>ⓢ</span><span>ⓛ</span></div>
  </div>
  <div class="field" style="left:414px;top:230px;width:147px;height:30px">Name</div>
  <div class="field" style="left:570px;top:230px;width:147px;height:30px">Phone</div>
  <div class="field" style="left:414px;top:270px;width:303px;height:80px">Message</div>
  <div class="btn" style="left:414px;top:362px;width:303px;height:38px">Send us</div>
  <div class="abs" role="img" aria-label="Map of the workshop location" style="left:818px;top:230px;width:303px;height:172px;background:linear-gradient(135deg,#e7ecdf,#cfd9e6);border:6px solid #fff"></div>
</footer>

<div class="abs bottom">
  <div class="abs" style="left:79px;top:20px">Copyright © 2019 Veltrashine - All Right Reserved</div>
  <div class="pay" style="left:912px;background:#1d3f8a">COINSEND</div>
  <div class="pay" style="left:968px;background:#1a2a8c">NORVIA</div>
  <div class="pay" style="left:1024px;background:#333">CARDENO</div>
  <div class="pay" style="left:1080px;background:#2a6ac4">AMPLO</div>
</div>

</body>
</html>
```